Escrow Accounting firm needs a website design for a startup that services clients nationally.

I offer escrow accounting services for title companies and real estate attorneys. I've enclosed a logo, color palette and flyers with content that can be used for the site.

I'm looking for a similar design concept as the website below from my former employer. Please don't copy because of copyright infringement. Including for design ideas only.
www.harborlinefiduciary.com

Below is a brief write-up...
For professionals in the title insurance industry, finding a trustworthy and budget-friendly solution for escrow accounting can be daunting. When choosing the right accounting partner, title companies and law firms need a group they can rely on, and that's where we come in.

```html
<!DOCTYPE html>
<html lang="en">
<head>
<meta charset="utf-8">
<title>Meridian Escrow Solutions</title>
<link href="https://fonts.googleapis.com/css2?family=Montserrat:ital,wght@0,400;0,500;0,600;0,700;0,800;0,900;1,800;1,900&family=Roboto:wght@400;500;700&display=swap" rel="stylesheet">
<style>
:root{
  --clay:#bb6f5f;
  --clay-soft:#e6c6bd;
  --navy:#353d4c;
  --ink:#3a3f4a;
  --text:#555b66;
  --line:#d9a596;
  --white:#ffffff;
  --mist:#eef0f2;
}
*{margin:0;padding:0;box-sizing:border-box}
html,body{width:1200px;height:3774px;overflow:hidden}
body{position:relative;background:var(--white);font-family:'Roboto',sans-serif;color:var(--text)}
.abs{position:absolute}
.heading{font-family:'Montserrat',sans-serif;font-weight:900;color:var(--navy);text-transform:uppercase;line-height:1.02}
.accent{color:var(--clay)}
.eyebrow{font-family:'Montserrat',sans-serif;font-weight:700;font-size:9px;letter-spacing:.5px;color:var(--clay);text-transform:uppercase}
.divider{display:flex;align-items:center;gap:12px}
.divider span.rule{flex:1;height:1px;background:var(--line)}
.divider span.dot{width:14px;height:14px;border:2px solid var(--clay);transform:rotate(45deg)}

/* top bar */
.topbar{left:0;top:0;width:1200px;height:28px;background:var(--clay);color:var(--white);font-size:10px}
.topbar .item{position:absolute;top:8px;display:flex;align-items:center;gap:6px}
.ring{width:14px;height:14px;border:1px solid var(--white);border-radius:50%;display:inline-block}
.topbar .socials{position:absolute;right:112px;top:6px;display:flex;gap:5px}
.topbar .socials .ring{width:16px;height:16px}

/* nav */
.brand{display:flex;align-items:center;gap:10px;font-family:'Montserrat',sans-serif;font-weight:500;color:var(--clay);text-transform:uppercase}
.brand .mark{width:26px;height:26px;border:3px solid var(--clay)}
.nav{left:112px;top:28px;width:976px;height:84px}
.nav .brand{position:absolute;left:0;top:24px;font-size:22px;letter-spacing:.5px}
.menu{position:absolute;left:338px;top:36px;display:flex;gap:14px;align-items:center;font-family:'Montserrat',sans-serif;font-size:11px;font-weight:600;color:var(--ink)}
.menu .sep{width:4px;height:4px;background:var(--clay);transform:rotate(45deg)}
.menu .active{color:var(--clay)}
.cta-top{position:absolute;right:0;top:24px;width:138px;height:38px;background:var(--clay);color:var(--white);border-radius:18px 0 18px 0;display:flex;align-items:center;justify-content:center;gap:6px;font-family:'Montserrat',sans-serif;font-size:10px;font-weight:700}

/* hero */
.hero-bg{left:0;top:112px;width:1200px;height:480px;background:linear-gradient(120deg,#e9ebee 0%,#f8f9fa 45%,#ffffff 70%)}
.hero-clay{left:728px;top:112px;width:472px;height:480px;background:var(--clay)}
.hero-photo{left:574px;top:150px;width:514px;height:400px;border-radius:90px 0 90px 0;background:linear-gradient(135deg,#6b8ea3 0%,#a9bfcb 45%,#2f3d52 100%)}
.hero-title{left:112px;top:210px;font-size:44px}
.hero-copy{left:114px;top:402px;width:330px;font-size:13.5px;line-height:1.45;color:var(--ink)}
.pager{left:114px;top:496px;display:flex;align-items:center;gap:14px;font-family:'Montserrat',sans-serif;font-size:9px;color:#777}
.pager .on{width:34px;height:34px;border:1.5px solid var(--clay);border-radius:50%;display:flex;align-items:center;justify-content:center;font-size:14px;color:var(--clay)}

/* services */
.sec-head{left:0;width:1200px;text-align:center}
.services-title{font-size:28px;font-style:italic}
.card{background:var(--white);border-radius:10px;box-shadow:0 4px 18px rgba(0,0,0,.08)}
.svc{top:854px;width:311px;height:336px;text-align:center}
.svc h3{margin-top:28px;font-family:'Roboto',sans-serif;font-weight:500;font-size:12.5px;color:var(--ink);text-transform:uppercase}
.svc .photo{margin:14px auto 0;width:282px;height:168px;border-radius:10px}
.svc p{margin:22px 28px 0;font-size:10.5px;line-height:1.7}
.btn{background:var(--clay);color:var(--white);font-family:'Montserrat',sans-serif;font-weight:700;font-size:10px;border-radius:18px 0 18px 0;display:flex;align-items:center;justify-content:center;gap:8px;text-transform:uppercase}

/* about */
.about-photo{left:112px;top:1430px;width:478px;height:446px;background:linear-gradient(160deg,#c78d7f 0%,#e7e3e0 40%,#4a5568 80%,#f3f3f3 100%)}
.callbar{left:143px;top:1870px;width:433px;height:42px;background:var(--clay);color:var(--white);border-radius:18px 0 18px 0;font-family:'Roboto',sans-serif;font-weight:500;font-size:13.5px;display:flex;align-items:center;justify-content:center}
.about-body{left:654px;top:1434px;width:434px}
.about-body h2{font-size:30px;margin-top:14px}
.about-body .lead{margin-top:40px;font-size:16px;line-height:1.35;color:var(--ink)}
.about-body p.small{margin-top:14px;font-size:10.5px;line-height:1.75}
.about-body p.mid{margin-top:22px;font-size:15px;line-height:1.4;color:var(--ink)}
.tabs{margin-top:22px;height:42px;border:1px solid var(--clay);display:flex;font-family:'Roboto',sans-serif;font-weight:500;font-size:12px;color:var(--ink)}
.tabs div{flex:1;display:flex;align-items:center;justify-content:center;border-bottom:3px solid var(--clay);margin:0 4px}

/* why */
.why-bg{left:0;top:2046px;width:680px;height:660px;background:var(--clay);border-radius:0 160px 0 160px}
.why-title{left:112px;top:2262px;font-size:28px;color:var(--white)}
.why-rule{left:112px;top:2362px;width:306px}
.why-rule .rule{background:rgba(255,255,255,.8)}
.why-rule .dot{border-color:var(--white)}
.why-call{left:112px;top:2430px;color:var(--white);font-family:'Montserrat',sans-serif}
.why-call .k{font-weight:600;font-size:14px}
.why-call .n{font-weight:800;font-size:36px;margin-top:2px}
.feat{width:273px;height:230px;border-radius:0 0 30px 0;padding:62px 26px 0}
.feat .badge{position:absolute;left:34px;top:-26px;width:62px;height:62px;border-radius:50%;background:var(--white);border:2px solid var(--clay);display:flex;align-items:center;justify-content:center}
.feat h4{font-family:'Roboto',sans-serif;font-weight:500;font-size:13px;color:var(--clay);text-transform:uppercase}
.feat p{margin-top:14px;font-size:10.5px;line-height:1.75}

/* testimonials */
.quote{left:356px;top:3008px;width:488px;text-align:center;font-size:10.5px;line-height:1.7;color:var(--ink)}
.avatar{left:563px;top:2932px;width:73px;height:73px;border-radius:50%;background:radial-gradient(circle at 50% 40%,#a07a68,#3b2c2a)}
.arrow{top:3007px;display:flex;align-items:center}

/* footer */
.foot{left:0;top:3270px;width:1200px;height:504px;background:var(--navy)}
.form-box{left:643px;top:3222px;width:445px;height:498px;background:var(--clay);border-radius:90px 0 90px 0}
.foot .brand{position:absolute;left:112px;top:73px;font-size:30px}
.foot .brand .mark{width:34px;height:34px}
.foot h5{position:absolute;font-family:'Montserrat',sans-serif;font-weight:700;font-size:13px;color:var(--clay);text-transform:uppercase}
.contact-row{position:absolute;left:112px;display:flex;align-items:center;gap:10px;font-size:11px;color:var(--white);line-height:1.5}
.contact-row .ic{width:26px;height:26px;border-radius:50%;border:1px solid var(--clay);display:flex;align-items:center;justify-content:center}
.links{position:absolute;left:418px;top:234px;list-style:none;font-size:11px;color:var(--white)}
.links li{margin-bottom:20px;display:flex;align-items:center;gap:12px}
.links li::before{content:"";width:4px;height:4px;border-radius:50%;background:var(--clay)}
.copy{position:absolute;left:112px;top:422px;font-size:10px;color:#c8ccd3;line-height:1.6}
.fsocial{position:absolute;left:416px;top:416px;display:flex;gap:8px}
.fsocial span{width:32px;height:32px;border-radius:50%;border:1px solid #7d8594}
.form-inner{position:absolute;left:58px;top:44px;width:326px;color:var(--white)}
.form-inner h2{font-family:'Montserrat',sans-serif;font-weight:900;font-size:28px}
.form-inner .sub{font-size:10px;line-height:1.5;margin-top:6px}
.field{margin-top:20px;height:28px;border-bottom:1px solid rgba(255,255,255,.7);display:flex;justify-content:space-between;align-items:flex-start;font-size:10.5px}
.field .ring{width:20px;height:20px;border-color:rgba(255,255,255,.9)}
.field.dim{color:rgba(255,255,255,.7)}
.field.msg{height:54px}
.submit{margin-top:30px;height:40px;background:var(--navy);border-radius:18px 0 18px 0;display:flex;align-items:center;justify-content:center;gap:8px;font-weight:500;font-size:12px}
</style>
</head>
<body>

<!-- top bar -->
<div class="abs topbar">
  <div class="item" style="left:112px"><span class="ring"></span>Call Us: 555-014-2290</div>
  <div class="item" style="left:266px"><span class="ring"></span>Email: hello@meridianescrow.com</div>
  <div class="socials"><span class="ring"></span><span class="ring"></span><span class="ring"></span></div>
</div>

<!-- navigation -->
<header class="abs nav">
  <div class="brand"><span class="mark"></span>Meridian Escrow</div>
  <nav class="menu">
    <span class="active">HOME</span><span class="sep"></span>
    <span>ABOUT US</span><span class="sep"></span>
    <span>SERVICES</span><span class="sep"></span>
    <span>CONTACT US</span>
  </nav>
  <div class="cta-top">
    <svg width="12" height="12" viewBox="0 0 24 24" fill="#fff"><path d="M6.6 10.8a15 15 0 0 0 6.6 6.6l2.2-2.2a1 1 0 0 1 1-.25 11 11 0 0 0 3.6.6 1 1 0 0 1 1 1V20a1 1 0 0 1-1 1A17 17 0 0 1 3 4a1 1 0 0 1 1-1h3.5a1 1 0 0 1 1 1c0 1.25.2 2.45.6 3.6a1 1 0 0 1-.25 1z"/></svg>
    CONTACT US
  </div>
</header>

<!-- hero -->
<section>
  <div class="abs hero-bg"></div>
  <div class="abs hero-clay"></div>
  <div class="abs hero-photo" role="img" aria-label="Photo of a smiling businessman working on a laptop in a bright office"></div>
  <h1 class="abs heading hero-title">Your<br><span class="accent">Financial<br>Success,</span> Our<br>Expertise</h1>
  <p class="abs hero-copy">We offer a full suite of accounting services designed to streamline your financial operations and help you make informed decisions.</p>
  <div class="abs pager"><span class="on">01</span><span>02</span><span>03</span><span>04</span></div>
</section>

<!-- services -->
<section>
  <div class="abs sec-head" style="top:688px"><span class="eyebrow">Our Services</span></div>
  <h2 class="abs sec-head heading services-title" style="top:712px">Your <span class="accent">Trusted Partner</span> In<br>Financial Excellence</h2>
  <div class="abs divider" style="left:368px;top:786px;width:464px"><span class="rule"></span><span class="dot"></span><span class="rule"></span></div>

  <article class="abs card svc" style="left:112px">
    <h3>Escrow Reconciliation Service</h3>
    <div class="photo" role="img" aria-label="Photo of a team reviewing financial charts on a desk" style="background:linear-gradient(135deg,#2c3a5a,#6f86a8 55%,#d9dde4)"></div>
    <p>Curabitur tristique risus sed nisi lobortis, a mollis tellus finibus. Nunc vulputate dui sed ligulagra vida, at pulvinar turpis mollis.</p>
  </article>
  <article class="abs card svc" style="left:444px">
    <h3>Title Industry Best Practice Certification</h3>
    <div class="photo" role="img" aria-label="Photo of hands using a calculator beside paperwork and glasses" style="background:linear-gradient(135deg,#eef0f3,#b9c1cc 55%,#5d6878)"></div>
    <p>Curabitur tristique risus sed nisi lobortis, a mollis tellus finibus. Nunc vulputate dui sed ligulagra vida, at pulvinar turpis mollis.</p>
  </article>
  <article class="abs card svc" style="left:776px">
    <h3>Data Call Services</h3>
    <div class="photo" role="img" aria-label="Photo of a smiling support agent wearing a headset" style="background:linear-gradient(135deg,#c9d3dd,#7f8a96 50%,#2b2f38)"></div>
    <p>Curabitur tristique risus sed nisi lobortis, a mollis tellus finibus. Nunc vulputate dui sed ligulagra vida, at pulvinar turpis mollis.</p>
  </article>

  <div class="abs btn" style="left:505px;top:1255px;width:189px;height:44px">
    <svg width="14" height="14" viewBox="0 0 14 14"><circle cx="7" cy="7" r="7" fill="#fff"/><path d="M7 4v6M4 7h6" stroke="#bb6f5f" stroke-width="1.6"/></svg>
    View All Services
  </div>
</section>

<!-- about -->
<section>
  <div class="abs about-photo" role="img" aria-label="Photo of two smiling professionals standing together, one holding a tablet"></div>
  <div class="abs callbar">FOR ANY INQUIRIES CALL US TODAY: 555-014-2290</div>
  <div class="abs about-body">
    <span class="eyebrow">About Us</span>
    <h2 class="heading">Meridian <span class="accent">Escrow</span><br>Solutions</h2>
    <div class="divider" style="margin-top:14px"><span class="dot"></span><span class="rule"></span></div>
    <p class="lead" style="margin-top:24px">Our Team Of <span class="accent">Experienced Professionals</span> Is The Ideal Solution For Your Needs.</p>
    <p class="small" style="margin-top:18px">Meridian Escrow Solutions has accounting experts who understand the title industry and the importance of compliance, security, and implementing precise escrow accounting procedures along with timely monthly reporting.</p>
    <p class="small">Escrow accounting services are at the heart of what we do. Trust us to provide you with peace of mind. With Meridian Escrow Solutions, you can be confident that your escrow accounting will be secure, accurate, and in complete compliance with Underwriter Requirements and Best Practices.</p>
    <p class="mid">Put our knowledge and experience to work for you.<br>We want to help you achieve 100%</p>
    <div class="tabs"><div>COMPLIANCE</div><div>EFFICIENCY</div><div>INTEGRITY</div></div>
  </div>
</section>

<!-- why choose -->
<section>
  <div class="abs why-bg"></div>
  <h2 class="abs heading why-title">Why Choose<br>Meridian Escrow<br>Solutions</h2>
  <div class="abs divider why-rule"><span class="dot"></span><span class="rule"></span></div>
  <div class="abs why-call"><div class="k">FOR ANY INQUIRIES CALL US TODAY:</div><div class="n">555-014-2290</div></div>

  <article class="abs card feat" style="left:524px;top:2126px">
    <span class="badge"><svg width="30" height="26" viewBox="0 0 30 26" fill="#353d4c"><circle cx="9" cy="9" r="4"/><circle cx="21" cy="9" r="4"/><circle cx="15" cy="12" r="4.5"/><path d="M3 24c0-5 3-8 6-8s4 1 4 1-3 2-3 7zM27 24c0-5-3-8-6-8s-4 1-4 1 3 2 3 7zM8 26c0-6 3-9 7-9s7 3 7 9z"/></svg></span>
    <h4>Expertise You Can Trust</h4>
    <p>Daily two-way reconciliation is a Best Practice Standard. Let us create a customized package that ensures your compliance and protects your reporting from audit deficiencies.</p>
  </article>
  <article class="abs card feat" style="left:814px;top:2126px">
    <span class="badge"><svg width="28" height="28" viewBox="0 0 28 28" fill="#353d4c"><circle cx="12" cy="8" r="5"/><path d="M2 26c0-7 4-11 10-11 3 0 5 1 6 2v9z"/><circle cx="22" cy="21" r="5" fill="#bb6f5f"/></svg></span>
    <h4>Personalized Service</h4>
    <p>We perform reconciliations across all accounting software systems using secure protocols aligning with Title Industry Best Practice - Pillar 3 standards.</p>
  </article>
  <article class="abs card feat" style="left:524px;top:2402px">
    <span class="badge"><svg width="30" height="26" viewBox="0 0 30 26"><rect x="3" y="16" width="5" height="9" fill="#353d4c"/><rect x="10" y="12" width="5" height="13" fill="#353d4c"/><rect x="17" y="8" width="5" height="17" fill="#353d4c"/><path d="M3 12 L12 6 L17 8 L27 2" stroke="#bb6f5f" stroke-width="2" fill="none"/></svg></span>
    <h4>Comprehensive Solutions</h4>
    <p>Comprehensive daily and monthly reports will be delivered securely using SecureVault. These reports will include a detailed breakdown of items that may require your attention. We also manage the submission of reconciliations to underwriters.</p>
  </article>
  <article class="abs card feat" style="left:814px;top:2402px">
    <span class="badge"><svg width="30" height="28" viewBox="0 0 30 28"><circle cx="16" cy="8" r="7" fill="#bb6f5f"/><path d="M16 4v8M13.5 6h4a1.5 1.5 0 0 1 0 3h-3a1.5 1.5 0 0 0 0 3h4" stroke="#fff" stroke-width="1.3" fill="none"/><path d="M2 20h7l6 2h7l6-4v4l-9 6H2z" fill="#353d4c"/></svg></span>
    <h4>Commitment To Accuracy</h4>
    <p>Our affordable rates allow your company to significantly enhance efficiency with minimal investment and focus on what matters. Pricing is based on account activity volume, and we offer discounts for multiple accounts.</p>
  </article>
</section>

<!-- testimonials -->
<section>
  <h2 class="abs sec-head heading" style="top:2812px;font-size:28px">See What <span class="accent">Our Clients</span> Think</h2>
  <div class="abs divider" style="left:358px;top:2860px;width:484px"><span class="rule"></span><span class="dot"></span><span class="rule"></span></div>
  <div class="abs avatar" role="img" aria-label="Client portrait photo"></div>
  <div class="abs arrow" style="left:286px">
    <svg width="55" height="28" viewBox="0 0 55 28"><path d="M2 14h40M2 14l6-4M2 14l6 4" stroke="#d9a596" stroke-width="1.2" fill="none"/><circle cx="41" cy="14" r="13" fill="#ecd2ca"/></svg>
  </div>
  <div class="abs arrow" style="left:862px">
    <svg width="55" height="28" viewBox="0 0 55 28"><circle cx="14" cy="14" r="13" fill="#bb6f5f"/><path d="M14 14h39M53 14l-6-4M53 14l-6 4" stroke="#353d4c" stroke-width="1.2" fill="none"/></svg>
  </div>
  <p class="abs quote">I recently engaged for our accounting needs, and the experience has been exceptional. From the initial consultation to the ongoing support, their team has demonstrated unparalleled professionalism and expertise.</p>
  <div class="abs sec-head" style="top:3083px;font-family:'Montserrat',sans-serif;font-size:18px;color:var(--ink)">Dana R.</div>
  <div class="abs sec-head" style="top:3108px;color:var(--clay);font-size:12px;letter-spacing:2px">★★★★★</div>
</section>

<!-- footer -->
<footer class="abs foot">
  <div class="brand"><span class="mark"></span>Meridian Escrow</div>
  <h5 style="left:112px;top:176px">Contact Us</h5>
  <h5 style="left:416px;top:176px">Quick Link</h5>
  <div class="contact-row" style="top:224px"><span class="ic"><svg width="10" height="13" viewBox="0 0 10 13"><path d="M5 0a5 5 0 0 1 5 5c0 4-5 8-5 8S0 9 0 5a5 5 0 0 1 5-5z" fill="#bb6f5f"/><circle cx="5" cy="5" r="1.8" fill="#353d4c"/></svg></span><span>48 Harbor View Road<br>Suite 210, Lakeport 00000</span></div>
  <div class="contact-row" style="top:278px"><span class="ic"><svg width="12" height="9" viewBox="0 0 12 9"><rect width="12" height="9" rx="1" fill="#bb6f5f"/><path d="M0 1l6 4 6-4" stroke="#353d4c" fill="none"/></svg></span><span>hello@meridianescrow.com</span></div>
  <div class="contact-row" style="top:318px"><span class="ic"><svg width="11" height="11" viewBox="0 0 24 24" fill="#bb6f5f"><path d="M6.6 10.8a15 15 0 0 0 6.6 6.6l2.2-2.2a1 1 0 0 1 1-.25 11 11 0 0 0 3.6.6 1 1 0 0 1 1 1V20a1 1 0 0 1-1 1A17 17 0 0 1 3 4a1 1 0 0 1 1-1h3.5a1 1 0 0 1 1 1c0 1.25.2 2.45.6 3.6a1 1 0 0 1-.25 1z"/></svg></span><span>555-014-2290</span></div>
  <ul class="links"><li>Home</li><li>About Us</li><li>Services</li><li>Contact Us</li></ul>
  <p class="copy">Copyright© 2024 <span class="accent">Meridian Escrow Solutions.</span><br>All Rights Reserved.</p>
  <div class="fsocial"><span></span><span></span><span></span></div>
</footer>

<div class="abs form-box">
  <form class="form-inner">
    <h2>GET IN TOUCH</h2>
    <p class="sub">Contact us today for a consultation and embark on the journey to turn your construction dreams into a stunning reality.</p>
    <div class="field" style="margin-top:30px">Name<span class="ring"></span></div>
    <div class="field dim">Phone<span class="ring"></span></div>
    <div class="field dim">Email<span class="ring"></span></div>
    <div class="field dim msg">Message<span class="ring"></span></div>
    <div class="submit"><svg width="14" height="14" viewBox="0 0 24 24" fill="#fff"><path d="M2 11 22 2l-7 20-4-8z"/></svg>Submit</div>
  </form>
</div>

</body>
</html>
```